Dr Delwyn's Letterhead

I need a professional neat letterhead incorporating my professional information, university titles and qualifications. I have attached my 3 recent ones which contain all the necessary information that needs to be included. I am happy for the information to be a side bar left or right, or as a header/footer combination.

Hello all

I have now made a 2nd and 3rd prize so please submit

Reason: Now there is a 2nd and 3rd place so I can take 3 designs

University

```html
<!DOCTYPE html>
<html lang="en">
<head>
<meta charset="utf-8">
<title>Dr Tamsin Delwyn – Letterhead</title>
<link rel="stylesheet" href="https://fonts.googleapis.com/css2?family=Source+Sans+3:wght@300;400&display=swap">
<style>
  :root {
    --ink: #1d3f55;
    --ink-soft: #3d5a6e;
    --rule: #a9bcc8;
    --paper: #ffffff;
    --backdrop: #e6e8ea;
    --mark: #f3f4f5;
    --crest-gold: #d9a93a;
    --crest-blue: #2f4d8c;
    --crest-red: #b8323a;
  }
  * { box-sizing: border-box; margin: 0; padding: 0; }
  html, body {
    width: 1200px; height: 1000px; overflow: hidden;
    background: var(--backdrop);
    font-family: "Source Sans 3", "Frutiger", Arial, sans-serif;
    color: var(--ink);
  }
  .letterhead {
    position: absolute; left: 260px; top: 20px;
    width: 680px; height: 960px;
    background: var(--paper);
  }
  .identity { position: absolute; left: 30px; top: 26px; }
  .identity__name { font-weight: 400; font-size: 31px; letter-spacing: 0.3px; line-height: 1; }
  .identity__quals { font-weight: 300; font-size: 12.5px; margin-top: 4px; color: var(--ink-soft); }
  .locations {
    position: absolute; left: 380px; top: 30px;
    display: flex; font-size: 9.2px; letter-spacing: 0.4px;
    text-transform: uppercase; line-height: 16px; color: var(--ink-soft);
  }
  .locations__site { padding-right: 11px; }
  .locations__site + .locations__site { padding-left: 11px; padding-right: 0; border-left: 1px solid var(--rule); }
  .roles {
    position: absolute; left: 24px; right: 18px; top: 85px;
    border-top: 1px solid var(--rule); border-bottom: 1px solid var(--rule);
    padding: 6px 0 5px; text-align: center;
    font-size: 13px; letter-spacing: 2.4px; text-transform: uppercase; line-height: 18.5px;
  }
  .monogram {
    position: absolute; left: 8px; top: 395px; width: 672px; height: 310px;
    background: linear-gradient(90deg, var(--mark), #f7f8f8 45%, var(--mark));
    opacity: 0.7;
  }
  .affiliations {
    position: absolute; left: 0; right: 0; top: 843px;
    display: flex; justify-content: center; align-items: center; gap: 14px;
  }
  .affiliations svg { display: block; }
  .college { display: flex; align-items: center; gap: 6px; font-size: 26px; font-weight: 400; letter-spacing: 0.5px; color: var(--crest-blue); }
  .practice-footer {
    position: absolute; left: 0; right: 0; top: 900px;
    text-align: center; font-size: 10.2px; line-height: 18px; color: var(--ink-soft);
  }
</style>
</head>
<body>
  <main class="letterhead">
    <header>
      <div class="identity">
        <h1 class="identity__name">Dr. Tamsin Delwyn</h1>
        <p class="identity__quals">BSc (Med) MBBS (Hons 1) UHC ACOS (Oto)</p>
      </div>
      <div class="locations">
        <address class="locations__site" style="font-style:normal">212/48 Carrow Road<br>Specialist Medical Centre<br>Elmsford NSW 2190</address>
        <address class="locations__site" style="font-style:normal">27 Linden Highway<br>Linden Specialist Centre<br>Ashcombe NSW 2176</address>
      </div>
      <div class="roles">
        Adult and Paediatric ENT | Head and Neck Surgery<br>
        Consultant &amp; Senior Lecturer | University of Harbourside<br>
        Elmsford Hospital and Area Health Service
      </div>
    </header>

    <div class="monogram" role="img" aria-label="Faint large initials monogram watermark"></div>

    <footer>
      <div class="affiliations">
        <svg width="44" height="40" viewBox="0 0 44 40" aria-hidden="true"><rect x="4" y="4" width="36" height="32" rx="6" fill="var(--crest-gold)"/></svg>
        <svg width="34" height="42" viewBox="0 0 34 42" aria-hidden="true"><path d="M2 2h30v20c0 10-8 16-15 18C10 38 2 32 2 22z" fill="var(--crest-blue)"/></svg>
        <span class="college">
          <svg width="30" height="38" viewBox="0 0 30 38" aria-hidden="true"><rect x="3" y="3" width="24" height="32" fill="var(--crest-red)"/></svg>
          ACOS
        </span>
      </div>
      <div class="practice-footer">
        The Elmsford Public and Private Hospitals &nbsp;|&nbsp; Kestrel Private Hospital<br>
        Provider 3817740K, 582613TP, 582613WM &nbsp;|&nbsp; Tel: 95510274 / 95518830 Fax: 95529416<br>
        p 95510274 95518830 &nbsp;| &nbsp;&nbsp; f 95529416
      </div>
    </footer>
  </main>
</body>
</html>
```